Lena Business card

This card is to represent me as a coach and Vivamora facilitator
Double sided in colour
A beautiful, simple and elegant design that indicates movement and is modern, FRESH and uplifting. Please don’t use much black and use the attached Vivamora logo.
Preferred colours - white, lighter blues and fresh greens

Target Market(s)
Business people - potential clients age 35 up
Industry/Entity Type
Business
Requirements
Must have
-  Text for the front :
Lumivera Living
Lena Darrow
Biocentric Coach
Co-Director, Vivamora School of Australia
E: lena@vivamora.com.au
M: 0471 552 908.
W: vivamora.com.au
Biocentric Coaching for Individuals, Teams and Organisations
Vivamora for Children, Adults and Social development projects
Text for the back :
The Vivamora system facilitates the expression of human potential for health, happiness and humanity through music, movement and group interaction. It was developed by Emilio Vasca Orduña, a Chilean anthropologist and clinical psychologist, in 1976.
Creative use of the logo - integrating it within the design - e.g perhaps using it as the O in Vivamora,
Please feature the heron from the logo or a another elegant graceful stylized heron.

```html
<!DOCTYPE html>
<html lang="en">
<head>
<meta charset="utf-8">
<title>Lena Darrow – Business Card</title>
<link href="https://fonts.googleapis.com/css2?family=Source+Sans+3:wght@400;600;700&display=swap" rel="stylesheet">
<style>
  :root {
    --card-green: #8bbf3c;
    --heron-orange: #e8692a;
    --heron-cream: #f6e3d2;
    --text-white: #ffffff;
    --stage: #eef0ea;
  }
  * { margin: 0; padding: 0; box-sizing: border-box; }
  html, body {
    width: 1200px; height: 720px; overflow: hidden;
    background: var(--stage);
    font-family: "Source Sans 3", "Myriad Pro", Arial, sans-serif;
  }
  .sheet {
    width: 1200px; height: 720px;
    display: flex; align-items: center; justify-content: center; gap: 40px;
  }
  .card {
    position: relative;
    width: 560px; height: 342px;
    background: var(--card-green);
    color: var(--text-white);
    box-shadow: 0 4px 14px rgba(0,0,0,0.12);
    overflow: hidden;
  }

  /* Front */
  .heron-art {
    position: absolute; left: 34px; top: 64px;
    width: 220px; height: 220px;
    border-radius: 46% 54% 40% 60% / 50% 42% 58% 50%;
    background: radial-gradient(circle at 55% 45%, var(--heron-cream) 0%, #f0a36f 45%, var(--heron-orange) 100%);
    opacity: 0.95;
  }
  .front-text {
    position: absolute; left: 282px; top: 34px; right: 22px;
  }
  .brand-line {
    font-size: 19px; font-weight: 700; letter-spacing: 1.4px;
    margin-bottom: 10px;
  }
  .person-name { font-size: 18px; font-weight: 700; line-height: 1.1; }
  .person-role { font-size: 13px; line-height: 1.3; }
  .contact-list { list-style: none; margin-top: 14px; }
  .contact-list li {
    display: flex; align-items: center; gap: 8px;
    font-size: 13px; line-height: 1.65;
  }
  .contact-icon { width: 13px; height: 13px; flex: none; }
  .services { margin-top: 16px; font-size: 13px; line-height: 1.25; }
  .services p + p { margin-top: 8px; }

  /* Back */
  .logo-lockup {
    position: absolute; top: 58px; left: 0; right: 0;
    display: flex; align-items: center; justify-content: center; gap: 10px;
    color: var(--heron-orange);
    font-size: 24px; font-weight: 600; letter-spacing: 1px;
  }
  .logo-dot {
    width: 22px; height: 22px; border-radius: 50%;
    border: 2px solid var(--heron-orange);
  }
  .system-blurb {
    position: absolute; left: 40px; right: 40px; top: 196px;
    text-align: center; font-size: 14.5px; line-height: 1.55;
  }
</style>
</head>
<body>
<main class="sheet">

  <section class="card card-front" aria-label="Card front">
    <div class="heron-art" role="img" aria-label="Stylised orange and cream heron in flight with spread wings"></div>
    <div class="front-text">
      <h1 class="brand-line">Lumivera Living</h1>
      <h2 class="person-name">Lena Darrow</h2>
      <p class="person-role">Biocentric Coach</p>
      <p class="person-role">Co-Director, Vivamora School of Australia</p>
      <ul class="contact-list">
        <li>
          <svg class="contact-icon" viewBox="0 0 14 14" aria-hidden="true"><rect x="3.5" y="1" width="7" height="12" rx="1.2" fill="none" stroke="#fff" stroke-width="1.4"/><rect x="5" y="3" width="4" height="6" fill="#fff"/></svg>
          0471 552 908
        </li>
        <li>
          <svg class="contact-icon" viewBox="0 0 14 14" aria-hidden="true"><circle cx="7" cy="7" r="6.5" fill="#fff"/><rect x="3.5" y="4.5" width="7" height="5" fill="none" stroke="#8bbf3c" stroke-width="1"/><path d="M3.5 4.5 7 7.5 10.5 4.5" fill="none" stroke="#8bbf3c" stroke-width="1"/></svg>
          lena@vivamora.com.au
        </li>
        <li>
          <svg class="contact-icon" viewBox="0 0 14 14" aria-hidden="true"><circle cx="7" cy="7" r="6" fill="none" stroke="#fff" stroke-width="1.3"/><ellipse cx="7" cy="7" rx="2.6" ry="6" fill="none" stroke="#fff" stroke-width="1"/><line x1="1" y1="7" x2="13" y2="7" stroke="#fff" stroke-width="1"/></svg>
          www.vivamora.com.au
        </li>
      </ul>
      <div class="services">
        <p>Biocentric Coaching for Individuals<br>Teams and Organisations</p>
        <p>Vivamora for Children, Adults and<br>Social development projects</p>
      </div>
    </div>
  </section>

  <section class="card card-back" aria-label="Card back">
    <div class="logo-lockup">
      <span class="logo-dot"></span>
      <span class="logo-name">Vivamora</span>
    </div>
    <p class="system-blurb">The Vivamora system facilitates the expression of human potential for health, happiness and humanity through music, movement and group interaction. It was developed by Emilio Vasca Orduña, a Chilean anthropologist and clinical psychologist, in 1976.</p>
  </section>

</main>
</body>
</html>
```